velumora.eu :: Design ideas (no coding) for key pages of Personalized greeting cards online store

We need your vision on modern, clean, easy to read user interface (UI) for online service of personalized printed products, like greeting cards, postcards, fridge magnets, clips and etc.
Your vision should include UI presentation for:
- Home page with login (including soc nets)
- Product Designer page
- Cart pages (products and address selection)
- Example of general internal page (pricing, terms, etc)
- Artist info and portfolio page
We are looking for ideas we will love, NOT complete design of a whole site.
Top design/vision will we used as a basement for separate contract on complete design of the site.

UI should be based on existing functionality with some extent. It should not break ideas or methods used on prototype but designers are free to offer own product presentations, designer’s layout and cart views.

Prototype:
English: http://velumora.eu
Russian: http://velumora.ru
Lithuanian: http://velumora.lt

Target Market(s)

People of 16-45 y.o. who likes to be distinctive, personal.

Industry/Entity Type

Store

Requirements
Must have
• Your work should meet attached requirements.
Site is multilingual. Wording should assume varieties in length on different languages.
Clean and easy to read UI
Flat design preferrably
Should be based on assets which are free or available for royalty-free licensing
Should not have
• heavy, meaningless 3D and shadow effects
Show NOT copy sites like: kindlow.com, tarnbell.co.uk

```html
<!DOCTYPE html>
<html lang="en">
<head>
<meta charset="utf-8">
<title>velumora — Greeting Cards Store</title>
<link rel="stylesheet" href="https://fonts.googleapis.com/css2?family=Open+Sans:wght@400;600&family=Arimo:wght@400&display=swap">
<style>
  :root {
    --teal: #1f9490;
    --teal-dark: #1a807c;
    --brand-red: #8f1d14;
    --accent: #f4915f;
    --ink: #111111;
    --text: #333333;
    --muted: #8a8a8a;
    --tag: #9a9a9a;
    --line: #dcdcdc;
    --input-line: #c8c8c8;
    --white: #ffffff;
    --star-off: #a5a5a5;
  }
  * { box-sizing: border-box; margin: 0; padding: 0; }
  html, body { width: 1200px; height: 2222px; overflow: hidden; background: var(--white); }
  body { position: relative; font-family: "Open Sans", Arial, sans-serif; color: var(--text); }
  .abs { position: absolute; }

  /* top login bar */
  .login-bar { top: 9px; left: 558px; display: flex; align-items: center; height: 22px; font-size: 12px; }
  .login-bar .login-label { display: flex; align-items: center; gap: 5px; font-size: 14px; color: #555; margin-right: 12px; font-family: Arimo, Arial, sans-serif; }
  .login-bar .field { width: 111px; height: 20px; border: 1px solid var(--input-line); font-size: 11px; padding: 3px 5px; color: #555; margin-right: 5px; font-family: Arimo, Arial, sans-serif; }
  .login-bar .submit { width: 63px; height: 20px; background: var(--brand-red); color: var(--white); font-size: 11px; text-align: center; line-height: 20px; margin-right: 18px; font-family: Arimo, Arial, sans-serif; }
  .login-bar .account-links { font-size: 11px; color: var(--muted); font-family: Arimo, Arial, sans-serif; }

  /* header */
  .header-tools { top: 85px; left: 190px; font-size: 11px; color: #777; line-height: 22px; }
  .header-tools .row { display: flex; align-items: center; gap: 5px; }
  .lang-mark { width: 14px; height: 9px; background: #c9cbd6; margin-left: 5px; }
  .brand { top: 52px; left: 494px; display: flex; flex-direction: column; align-items: center; gap: 6px; width: 112px; }
  .brand-square { width: 62px; height: 62px; background: var(--teal); }
  .brand-name { font-size: 20px; color: var(--brand-red); font-weight: 400; letter-spacing: 0.5px; line-height: 1; }
  .cart { top: 94px; left: 898px; display: flex; align-items: center; gap: 8px; font-size: 15px; color: #777; font-family: Arimo, Arial, sans-serif; }

  /* navigation */
  .main-nav { top: 158px; left: 0; width: 1200px; height: 49px; background: var(--teal); }
  .main-nav ul { position: absolute; left: 190px; top: 0; height: 49px; display: flex; list-style: none; }
  .main-nav li { color: var(--white); font-size: 14.5px; line-height: 49px; padding: 0 14px; border-left: 1px solid var(--teal-dark); font-family: Arimo, Arial, sans-serif; }
  .main-nav li:first-child { padding-left: 0; border-left: none; }
  .social-top { position: absolute; left: 914px; top: 11px; display: flex; gap: 3px; }
  .social-top span { width: 30px; height: 28px; background: var(--white); display: flex; align-items: center; justify-content: center; }
  .social-top i { width: 12px; height: 12px; background: var(--brand-red); display: block; }

  /* hero */
  .hero { top: 207px; left: 0; width: 1200px; height: 275px; border-bottom: 1px solid var(--line); }
  .hero-divider { top: 207px; left: 440px; width: 1px; height: 274px; background: var(--line); }
  .slogan { top: 254px; left: 190px; width: 240px; font-size: 34px; line-height: 40px; color: var(--brand-red); }
  .filter-title { top: 238px; left: 476px; font-size: 14.5px; color: var(--brand-red); font-family: Arimo, Arial, sans-serif; }
  .filter-box { left: 474px; width: 536px; height: 39px; border: 1px solid var(--input-line); display: flex; align-items: center; justify-content: space-between; padding: 0 14px 0 15px; font-size: 14px; color: var(--muted); font-family: Arimo, Arial, sans-serif; }
  .tag-cloud { left: 476px; width: 540px; font-family: Arimo, Arial, sans-serif; color: var(--tag); }
  .tag-row { display: flex; align-items: baseline; gap: 13px; white-space: nowrap; }
  .t-s { font-size: 13px; }
  .t-m { font-size: 21px; }
  .t-l { font-size: 35px; }

  /* products */
  .section-title { top: 519px; left: 0; width: 1200px; text-align: center; font-size: 27px; color: var(--ink); font-family: Arimo, Arial, sans-serif; }
  .product-row { left: 190px; width: 820px; height: 430px; display: flex; }
  .product { position: relative; width: 205px; height: 430px; text-align: center; }
  .product-title { position: absolute; top: 0; left: 0; width: 205px; font-size: 15.5px; line-height: 22px; color: var(--ink); }
  .product-art { position: absolute; left: 50%; transform: translateX(-50%); }
  .art-portrait { top: 55px; width: 138px; height: 200px; }
  .art-wide { top: 53px; width: 164px; height: 125px; }
  .art-square { top: 53px; width: 158px; height: 145px; }
  .fold { position: absolute; top: 0; left: 6%; width: 88%; height: 10px; background: #b8b7d6; }
  .face { position: absolute; top: 8px; left: 0; right: 0; bottom: 0; }
  .tone-beige { background: linear-gradient(160deg, #f1d4a2, #e9c48c 60%, #dcae74); }
  .tone-grey { background: linear-gradient(160deg, #d8d8d6, #9e9e9c 55%, #6c6c6a); }
  .tone-snow { background: linear-gradient(150deg, #f3ebe4, #e6d8cc 60%, #d8c3b3); }
  .tone-rose { background: linear-gradient(150deg, #f2b6a6, #d98b7e 50%, #9fae88); }
  .old-price { position: absolute; top: 268px; left: 0; width: 205px; font-size: 15px; color: #777; text-decoration: line-through; }
  .price { position: absolute; top: 290px; left: 0; width: 205px; font-size: 26px; color: var(--ink); }
  .rating { position: absolute; top: 333px; left: 0; width: 205px; display: flex; justify-content: center; gap: 2px; }
  .rating svg { width: 11px; height: 11px; }
  .product.is-active { background: var(--accent); height: 428px; margin-top: -46px; }
  .product.is-active .product-title { top: 46px; color: var(--white); }
  .product.is-active .old-price { top: 314px; color: #fbe2d4; }
  .product.is-active .price { top: 336px; color: var(--white); }
  .product.is-active .rating { top: 379px; }
  .btn { position: absolute; left: 36px; width: 132px; height: 45px; background: var(--brand-red); color: var(--white); font-size: 15.5px; line-height: 45px; }
  .row-line { left: 190px; width: 820px; height: 1px; background: var(--line); }

  /* footer */
  .footer-line { top: 1969px; left: 0; width: 1200px; height: 1px; background: var(--line); }
  .footer-mark { top: 1961px; left: 592px; }
  .footer-links { top: 2003px; left: 0; width: 1200px; text-align: center; font-size: 11.5px; color: #666; }
  .copyright { top: 2027px; left: 0; width: 1200px; text-align: center; font-size: 11.5px; color: #777; }
  .play { top: 2065px; left: 577px; }
  .social-foot { top: 2130px; left: 558px; display: flex; align-items: center; }
  .social-foot span { width: 28px; height: 28px; display: flex; align-items: center; justify-content: center; }
  .social-foot span + span { border-left: 1px solid var(--line); }
  .social-foot i { width: 11px; height: 11px; background: var(--brand-red); display: block; }
</style>
</head>
<body>

<!-- login bar -->
<div class="abs login-bar">
  <span class="login-label">
    <svg width="12" height="14" viewBox="0 0 12 14"><path d="M3 6V4a3 3 0 0 1 6 0v2" fill="none" stroke="#666" stroke-width="1.6"/><rect x="1" y="6" width="10" height="8" rx="1" fill="#666"/></svg>
    Login
  </span>
  <span class="field">Username</span>
  <span class="field">Password</span>
  <span class="submit">Submit</span>
  <span class="account-links">Signup &nbsp;/&nbsp; Help</span>
</div>

<!-- header -->
<div class="abs header-tools">
  <div class="row">Favorites (0)
    <svg width="11" height="10" viewBox="0 0 11 10"><path d="M0 4.5 5.5 0 11 4.5V10H0Z" fill="#8a8a96"/></svg>
  </div>
  <div class="row"><span class="lang-mark"></span>English
    <svg width="12" height="12" viewBox="0 0 12 12"><circle cx="6" cy="6" r="6" fill="#8a8a96"/><path d="M3.3 4.8 6 7.4 8.7 4.8" fill="none" stroke="#fff" stroke-width="1.5"/></svg>
  </div>
</div>

<div class="abs brand">
  <span class="brand-square"></span>
  <span class="brand-name">velumora</span>
</div>

<div class="abs cart">
  <svg width="32" height="24" viewBox="0 0 32 24"><path d="M1 2h5l4 14h16l4-10H8" fill="none" stroke="#8a8a96" stroke-width="2.2" stroke-linejoin="round"/><circle cx="12" cy="21" r="2" fill="#8a8a96"/><circle cx="24" cy="21" r="2" fill="#8a8a96"/></svg>
  CART (0)
</div>

<!-- navigation -->
<nav class="abs main-nav">
  <ul>
    <li>All Medias</li>
    <li>Greeting Cards</li>
    <li>Square Cards</li>
    <li>Postcards</li>
    <li>Contact</li>
  </ul>
  <div class="social-top">
    <span><i></i></span><span><i></i></span><span><i></i></span>
  </div>
</nav>

<!-- hero with filter -->
<div class="abs hero"></div>
<div class="abs hero-divider"></div>
<p class="abs slogan">Lorem Ipsum dummy slogan comse here !</p>

<p class="abs filter-title">Products Filter</p>
<div class="abs filter-box" style="top:262px">
  By Colors
  <svg width="14" height="9" viewBox="0 0 14 9"><path d="M1 1l6 6 6-6" fill="none" stroke="#666" stroke-width="2.2"/></svg>
</div>
<div class="abs filter-box" style="top:305px">
  Keyword Search
  <svg width="13" height="13" viewBox="0 0 13 13"><path d="M6.5 0v13M0 6.5h13" stroke="#666" stroke-width="1.6"/></svg>
</div>

<div class="abs tag-cloud" style="top:355px">
  <div class="tag-row">
    <span class="t-s">Bears</span><span class="t-m">Birthday</span><span class="t-l">Cards</span><span class="t-s">Cats</span><span class="t-m">Conratulations</span><span class="t-s" style="margin-left:6px">Dogs</span>
  </div>
</div>
<div class="abs tag-cloud" style="top:393px">
  <div class="tag-row">
    <span class="t-m">Newborn</span><span class="t-l">Flowers</span><span class="t-m">Birthday</span><span class="t-s">Friendship</span><span class="t-l">Cards</span>
  </div>
</div>

<!-- products -->
<h2 class="abs section-title" style="font-weight:400">Lorem Products</h2>

<svg width="0" height="0" style="position:absolute">
  <defs>
    <symbol id="pip" viewBox="0 0 11 11"><path d="M0 4.5 5.5 0 11 4.5V11H0Z"/></symbol>
  </defs>
</svg>

<!-- row 1 -->
<div class="abs product-row" style="top:634px">
  <div class="product">
    <p class="product-title">Lorem Ipsum<br>Card Title</p>
    <div class="product-art art-portrait" role="img" aria-label="Folded card with floral pattern and leaf bouquet illustration"><span class="fold"></span><span class="face tone-beige"></span></div>
    <p class="old-price">€ 1.20</p><p class="price">€ 0.99</p>
    <div class="rating"><svg fill="#8f1d14"><use href="#pip"/></svg><svg fill="#8f1d14"><use href="#pip"/></svg><svg fill="#8f1d14"><use href="#pip"/></svg><svg fill="#a5a5a5"><use href="#pip"/></svg><svg fill="#a5a5a5"><use href="#pip"/></svg></div>
  </div>
  <div class="product is-active">
    <p class="product-title">Lorem Ipsum<br>Card Title</p>
    <span class="btn" style="top:129px">Add to Cart</span>
    <span class="btn" style="top:179px">More Dtails</span>
    <p class="old-price">€ 1.20</p><p class="price">€ 0.99</p>
    <div class="rating"><svg fill="#8f1d14"><use href="#pip"/></svg><svg fill="#8f1d14"><use href="#pip"/></svg><svg fill="#8f1d14"><use href="#pip"/></svg><svg fill="#8f1d14"><use href="#pip"/></svg><svg fill="#8f1d14"><use href="#pip"/></svg></div>
  </div>
  <div class="product">
    <p class="product-title">Lorem Ipsum<br>Card Title</p>
    <div class="product-art art-wide" role="img" aria-label="Wide card with small whimsical winter creatures illustration"><span class="fold"></span><span class="face tone-snow"></span></div>
    <p class="old-price">€ 1.20</p><p class="price">€ 0.99</p>
    <div class="rating"><svg fill="#8f1d14"><use href="#pip"/></svg><svg fill="#8f1d14"><use href="#pip"/></svg><svg fill="#8f1d14"><use href="#pip"/></svg><svg fill="#a5a5a5"><use href="#pip"/></svg><svg fill="#a5a5a5"><use href="#pip"/></svg></div>
  </div>
  <div class="product">
    <p class="product-title">Lorem Ipsum<br>Card Title</p>
    <div class="product-art art-square" role="img" aria-label="Square card with swirling tree and red berries illustration"><span class="fold"></span><span class="face tone-rose"></span></div>
    <p class="old-price">€ 1.20</p><p class="price">€ 0.99</p>
    <div class="rating"><svg fill="#8f1d14"><use href="#pip"/></svg><svg fill="#8f1d14"><use href="#pip"/></svg><svg fill="#8f1d14"><use href="#pip"/></svg><svg fill="#a5a5a5"><use href="#pip"/></svg><svg fill="#a5a5a5"><use href="#pip"/></svg></div>
  </div>
</div>

<div class="abs row-line" style="top:1043px"></div>

<!-- row 2 -->
<div class="abs product-row" style="top:1084px">
  <div class="product">
    <p class="product-title">Lorem Ipsum<br>Card Title</p>
    <div class="product-art art-portrait" role="img" aria-label="Folded card with floral pattern and leaf bouquet illustration"><span class="fold"></span><span class="face tone-beige"></span></div>
    <p class="old-price">€ 1.20</p><p class="price">€ 0.99</p>
    <div class="rating"><svg fill="#8f1d14"><use href="#pip"/></svg><svg fill="#8f1d14"><use href="#pip"/></svg><svg fill="#8f1d14"><use href="#pip"/></svg><svg fill="#a5a5a5"><use href="#pip"/></svg><svg fill="#a5a5a5"><use href="#pip"/></svg></div>
  </div>
  <div class="product">
    <p class="product-title">Lorem Ipsum<br>Card Title</p>
    <div class="product-art art-portrait" role="img" aria-label="Folded card with black and white animal photograph"><span class="fold"></span><span class="face tone-grey"></span></div>
    <p class="old-price">€ 1.20</p><p class="price">€ 0.99</p>
    <div class="rating"><svg fill="#8f1d14"><use href="#pip"/></svg><svg fill="#8f1d14"><use href="#pip"/></svg><svg fill="#8f1d14"><use href="#pip"/></svg><svg fill="#a5a5a5"><use href="#pip"/></svg><svg fill="#a5a5a5"><use href="#pip"/></svg></div>
  </div>
  <div class="product">
    <p class="product-title">Lorem Ipsum<br>Card Title</p>
    <div class="product-art art-wide" role="img" aria-label="Wide card with small whimsical winter creatures illustration"><span class="fold"></span><span class="face tone-snow"></span></div>
    <p class="old-price">€ 1.20</p><p class="price">€ 0.99</p>
    <div class="rating"><svg fill="#8f1d14"><use href="#pip"/></svg><svg fill="#8f1d14"><use href="#pip"/></svg><svg fill="#8f1d14"><use href="#pip"/></svg><svg fill="#a5a5a5"><use href="#pip"/></svg><svg fill="#a5a5a5"><use href="#pip"/></svg></div>
  </div>
  <div class="product">
    <p class="product-title">Lorem Ipsum<br>Card Title</p>
    <div class="product-art art-square" role="img" aria-label="Square card with swirling tree and red berries illustration"><span class="fold"></span><span class="face tone-rose"></span></div>
    <p class="old-price">€ 1.20</p><p class="price">€ 0.99</p>
    <div class="rating"><svg fill="#8f1d14"><use href="#pip"/></svg><svg fill="#8f1d14"><use href="#pip"/></svg><svg fill="#8f1d14"><use href="#pip"/></svg><svg fill="#a5a5a5"><use href="#pip"/></svg><svg fill="#a5a5a5"><use href="#pip"/></svg></div>
  </div>
</div>

<div class="abs row-line" style="top:1481px"></div>

<!-- row 3 -->
<div class="abs product-row" style="top:1537px">
  <div class="product">
    <p class="product-title">Lorem Ipsum<br>Card Title</p>
    <div class="product-art art-portrait" role="img" aria-label="Folded card with floral pattern and leaf bouquet illustration"><span class="fold"></span><span class="face tone-beige"></span></div>
    <p class="old-price">€ 1.20</p><p class="price">€ 0.99</p>
    <div class="rating"><svg fill="#8f1d14"><use href="#pip"/></svg><svg fill="#8f1d14"><use href="#pip"/></svg><svg fill="#8f1d14"><use href="#pip"/></svg><svg fill="#a5a5a5"><use href="#pip"/></svg><svg fill="#a5a5a5"><use href="#pip"/></svg></div>
  </div>
  <div class="product">
    <p class="product-title">Lorem Ipsum<br>Card Title</p>
    <div class="product-art art-portrait" role="img" aria-label="Folded card with black and white animal photograph"><span class="fold"></span><span class="face tone-grey"></span></div>
    <p class="old-price">€ 1.20</p><p class="price">€ 0.99</p>
    <div class="rating"><svg fill="#8f1d14"><use href="#pip"/></svg><svg fill="#8f1d14"><use href="#pip"/></svg><svg fill="#8f1d14"><use href="#pip"/></svg><svg fill="#a5a5a5"><use href="#pip"/></svg><svg fill="#a5a5a5"><use href="#pip"/></svg></div>
  </div>
  <div class="product">
    <p class="product-title">Lorem Ipsum<br>Card Title</p>
    <div class="product-art art-wide" role="img" aria-label="Wide card with small whimsical winter creatures illustration"><span class="fold"></span><span class="face tone-snow"></span></div>
    <p class="old-price">€ 1.20</p><p class="price">€ 0.99</p>
    <div class="rating"><svg fill="#8f1d14"><use href="#pip"/></svg><svg fill="#8f1d14"><use href="#pip"/></svg><svg fill="#8f1d14"><use href="#pip"/></svg><svg fill="#a5a5a5"><use href="#pip"/></svg><svg fill="#a5a5a5"><use href="#pip"/></svg></div>
  </div>
  <div class="product">
    <p class="product-title">Lorem Ipsum<br>Card Title</p>
    <div class="product-art art-square" role="img" aria-label="Square card with swirling tree and red berries illustration"><span class="fold"></span><span class="face tone-rose"></span></div>
    <p class="old-price">€ 1.20</p><p class="price">€ 0.99</p>
    <div class="rating"><svg fill="#8f1d14"><use href="#pip"/></svg><svg fill="#8f1d14"><use href="#pip"/></svg><svg fill="#8f1d14"><use href="#pip"/></svg><svg fill="#a5a5a5"><use href="#pip"/></svg><svg fill="#a5a5a5"><use href="#pip"/></svg></div>
  </div>
</div>

<!-- footer -->
<div class="abs footer-line"></div>
<svg class="abs footer-mark" width="15" height="12" viewBox="0 0 15 12"><path d="M0 5 7.5 0 15 5V12H0Z" fill="#c4c4c4"/></svg>
<p class="abs footer-links">About Us &nbsp;-&nbsp; How it works &nbsp;-&nbsp; Prices &nbsp;-&nbsp; Rules &nbsp;-&nbsp; Contacts</p>
<p class="abs copyright">All Right Reserved © Co[pytight 2014</p>
<svg class="abs play" width="46" height="46" viewBox="0 0 46 46"><circle cx="23" cy="23" r="21.5" fill="none" stroke="#9a9a9a" stroke-width="2"/><path d="M18 14v18l14-9Z" fill="#8a8a8a"/></svg>
<div class="abs social-foot">
  <span><i></i></span><span><i></i></span><span><i></i></span>
</div>

</body>
</html>
```